Innovative tech company looking for a new look for business card

We need a business card revamp- our current design is amazingly dated and in need of a new vision. The Delta is logo that is used, but other than that and the company name - we are open to everything- red is the color of choice typically due to delta. VN is a National credit reporting agency servicing lending institutions for more than 24 years.

***We want a minimal, clean design, we want to move away from the harsh- red, black and white feel. The files uploaded are to show what we are currently using and exactly what we want to move AWAY from.

Thanks you to all!

We are looking for a "lighter" feel more "oriel-esque." We want to move away from the harsh black , white, and red. The files I uploaded were more to show what we currently have and really want to move away from. I am going to edit the brief to be sure this is expressed.

Reason: Still looking for options....

Reason: Still looking for more designs -

```html
<!DOCTYPE html>
<html lang="en">
<head>
<meta charset="utf-8">
<title>Vantor Nexus — Business Card</title>
<link href="https://fonts.googleapis.com/css2?family=Open+Sans:wght@400;600&display=swap" rel="stylesheet">
<style>
  :root {
    --bg-top: #f6f6f5;
    --bg-bottom: #e4e4e2;
    --card: #fbf9f7;
    --card-edge: #ece7e3;
    --accent: #e2645d;
    --accent-soft: #f2b6b1;
    --ink: #3d4248;
    --muted: #8c9197;
  }
  * { box-sizing: border-box; margin: 0; padding: 0; }
  html, body { width: 1200px; height: 1200px; overflow: hidden; }
  body {
    background: linear-gradient(160deg, var(--bg-top), var(--bg-bottom));
    font-family: "Open Sans", Arial, sans-serif;
    display: flex;
    flex-direction: column;
    align-items: center;
    justify-content: center;
    gap: 70px;
  }
  .card {
    position: relative;
    width: 630px;
    height: 360px;
    background: var(--card);
    border: 1px solid var(--card-edge);
    box-shadow: 0 12px 28px rgba(60, 50, 45, 0.12);
    overflow: hidden;
  }
  .rule { background: var(--accent-soft); }

  .brand-name {
    display: flex;
    align-items: center;
    gap: 10px;
    color: var(--ink);
    font-weight: 400;
    letter-spacing: 3px;
    text-transform: uppercase;
    white-space: nowrap;
  }
  .brand-dot { width: 12px; height: 12px; border-radius: 50%; background: var(--accent); flex: none; }
  .brand-tagline {
    color: var(--accent);
    text-align: right;
    margin-top: 2px;
    white-space: nowrap;
  }

  /* front */
  .front-band {
    position: absolute;
    left: 0; right: 0; top: 150px;
    display: flex;
    align-items: flex-start;
  }
  .front-band .rule { flex: 1; height: 2px; margin-top: 19px; }
  .front .brand { padding: 0 22px; }
  .front .brand-name { font-size: 30px; }
  .front .brand-tagline { font-size: 11px; }

  /* back */
  .back .rule-top { position: absolute; left: 50px; top: 0; width: 2px; height: 70px; }
  .back .rule-bottom { position: absolute; left: 50px; bottom: 0; width: 2px; height: 95px; }
  .back .brand { position: absolute; right: 40px; top: 120px; }
  .back .brand-name { font-size: 22px; letter-spacing: 2px; }
  .back .brand-tagline { font-size: 9px; }

  .contact { position: absolute; left: 70px; top: 88px; color: var(--ink); }
  .person-name { font-weight: 600; font-size: 17px; letter-spacing: 1px; }
  .person-role { color: var(--muted); font-size: 12px; margin-bottom: 14px; }
  .contact-list { list-style: none; }
  .contact-list li {
    display: flex;
    align-items: flex-start;
    gap: 10px;
    font-size: 14px;
    line-height: 1.35;
    margin-bottom: 5px;
  }
  .icon { flex: none; width: 16px; height: 16px; margin-top: 2px; }
  .icon-bg { fill: var(--accent); }
</style>
</head>
<body>

<section class="card front" aria-label="Card front">
  <div class="front-band">
    <span class="rule"></span>
    <div class="brand">
      <div class="brand-name"><span class="brand-dot"></span>Vantor Nexus</div>
      <div class="brand-tagline">Modern Credit Reporting &amp; Rescoring</div>
    </div>
    <span class="rule"></span>
  </div>
</section>

<section class="card back" aria-label="Card back">
  <span class="rule rule-top"></span>
  <span class="rule rule-bottom"></span>

  <div class="contact">
    <div class="person-name">XXXXXX XXXXXXXX</div>
    <div class="person-role">xxxxxxx</div>
    <ul class="contact-list">
      <li>
        <svg class="icon" viewBox="0 0 16 16"><circle class="icon-bg" cx="8" cy="8" r="8"/><path d="M8 3.5a2.6 2.6 0 0 0-2.6 2.6C5.4 8.2 8 12 8 12s2.6-3.8 2.6-5.9A2.6 2.6 0 0 0 8 3.5z" fill="#fff"/><circle class="icon-bg" cx="8" cy="6.1" r="1"/></svg>
        <span>xxxxxxx, xxxxxx, xx48,<br>xxxxxx xxxxx-454</span>
      </li>
      <li>
        <svg class="icon" viewBox="0 0 16 16"><circle class="icon-bg" cx="8" cy="8" r="8"/><rect x="5.5" y="3.5" width="5" height="9" rx="1" fill="#fff"/><rect class="icon-bg" x="6.3" y="4.6" width="3.4" height="5.6"/></svg>
        <span>xxxxxxxxxx</span>
      </li>
      <li>
        <svg class="icon" viewBox="0 0 16 16"><circle class="icon-bg" cx="8" cy="8" r="8"/><rect x="4" y="5" width="8" height="6" fill="#fff"/><path d="M4 5l4 3.2L12 5" stroke="#e2645d" stroke-width="1" fill="none"/></svg>
        <span>aaaaaa@xxxxxxx.com</span>
      </li>
      <li>
        <svg class="icon" viewBox="0 0 16 16"><circle class="icon-bg" cx="8" cy="8" r="8"/><circle cx="8" cy="8" r="4.2" stroke="#fff" stroke-width="1" fill="none"/><ellipse cx="8" cy="8" rx="1.8" ry="4.2" stroke="#fff" stroke-width="1" fill="none"/><path d="M3.8 8h8.4" stroke="#fff" stroke-width="1"/></svg>
        <span>www.vantornexus.com</span>
      </li>
    </ul>
  </div>

  <div class="brand">
    <div class="brand-name"><span class="brand-dot"></span>Vantor Nexus</div>
    <div class="brand-tagline">Modern Credit Reporting &amp; Rescoring</div>
  </div>
</section>

</body>
</html>
```